3rd Annual Maple & Clover Fundraiser

This is our 3rd Annual Maple & Clover Dog Wash Extravagana to support Circle of Harlow Ridge Pet Center. Please see the attached flyer for the 2nd Annual. We loved this flyer! Please revamp with our logo attached and the new content provided. Let's keep to the same colors as the 2nd Annual flyer-no change. Date: Saturday April 25th 2020 10A-1PM. Rain Date: May 2nd. Same address as 2nd Annual.

Other font styles liked:
• See 2nd Annual Flyer

Colors
add136
e34297
6b449b

Requirements
Must have
• See attached 2nd annual flyer including colors
Nice to have

```html
<!DOCTYPE html>
<html lang="en">
<head>
<meta charset="utf-8">
<title>Maple &amp; Clover Doggie Wash Extravaganza</title>
<link rel="stylesheet" href="https://fonts.googleapis.com/css2?family=Montserrat:ital,wght@0,600;0,700;0,800;0,900;1,600&family=Arimo:ital,wght@0,400;0,700;1,400&display=swap">
<style>
  :root {
    --green: #add136;
    --pink: #e34297;
    --purple: #6b449b;
    --ink: #333333;
    --white: #ffffff;
    --page: #f2f2f2;
  }
  * { box-sizing: border-box; margin: 0; padding: 0; }
  html, body { width: 1026px; height: 1200px; overflow: hidden; background: var(--page); }
  .flyer {
    position: relative; width: 1026px; height: 1200px; overflow: hidden;
    background: var(--white); font-family: "Arimo", Arial, sans-serif; color: var(--ink);
  }
  .hero-photo {
    position: absolute; left: 0; top: 0; width: 1026px; height: 470px;
    background: linear-gradient(160deg, #7d8a7c 0%, #a9a095 35%, #5a5c63 60%, #c9c4bb 100%);
  }
  .swoosh { position: absolute; left: 0; top: 0; width: 1026px; height: 1200px; }
  .spot-photo {
    position: absolute; width: 190px; height: 190px; border-radius: 50%;
    border: 6px solid var(--white); box-shadow: 0 2px 6px rgba(0,0,0,.25);
  }
  .spot-dog { left: 452px; top: 361px; background: radial-gradient(circle at 45% 45%, #7a5a3a, #b7a27a 60%, #8fae6a); }
  .spot-music { left: 642px; top: 361px; background: radial-gradient(circle at 50% 55%, #6f7d96, #d9d6d0 65%, #a7b0a3); }
  .spot-mascot { left: 830px; top: 361px; background: radial-gradient(circle at 55% 40%, #a8773e, #3f6fb0 60%, #c9c2b6); }

  .kicker { position: absolute; left: 42px; top: 512px; font: 800 30px/1 "Montserrat", sans-serif; color: var(--purple); }
  .title { position: absolute; left: 42px; top: 554px; font: 900 46px/1 "Montserrat", sans-serif; color: var(--pink); }
  .subtitle { position: absolute; left: 42px; top: 605px; font: 800 32px/1 "Montserrat", sans-serif; color: var(--green); }
  .tagline-pill {
    position: absolute; left: 0; top: 644px; width: 765px; height: 50px;
    background: var(--purple); border-radius: 0 25px 25px 0;
    font: 700 32px/50px "Montserrat", sans-serif; color: var(--white); padding-left: 52px;
  }

  .support { position: absolute; left: 790px; top: 564px; width: 236px; text-align: center; }
  .support-label { font: 800 24px/1 "Montserrat", sans-serif; color: #111; }
  .partner-name {
    display: flex; align-items: center; justify-content: center; gap: 8px;
    margin-top: 22px; font: 800 20px/1.15 "Montserrat", sans-serif; color: #111;
  }
  .partner-name .mark { flex: none; width: 16px; height: 16px; border-radius: 50%; background: #111; }
  .partner-note { margin-top: 22px; font: 700 13px/1.5 "Arimo", sans-serif; color: #111; }

  .details { position: absolute; font: 700 20px/1.3 "Arimo", sans-serif; }
  .details sup { font-size: 12px; line-height: 0; vertical-align: 8px; }
  .details .label { color: var(--pink); }
  .when { left: 42px; top: 706px; display: grid; grid-template-columns: 64px auto; }
  .time { left: 42px; top: 786px; display: grid; grid-template-columns: 64px auto; }
  .where { left: 434px; top: 706px; }

  .perks-band {
    position: absolute; left: 0; top: 828px; width: 1026px; height: 228px; background: var(--green);
  }
  .perks { position: absolute; list-style: none; font: 700 21px/1 "Arimo", sans-serif; color: var(--white); }
  .perks li { display: flex; align-items: center; gap: 12px; height: 37px; }
  .perks svg { width: 26px; height: 26px; flex: none; }
  .perks-left { left: 56px; top: 852px; }
  .perks-right { left: 450px; top: 852px; }
  .donate-line { position: absolute; left: 42px; top: 981px; font: 700 15px/1 "Arimo", sans-serif; color: var(--white); }
  .donate-button {
    position: absolute; left: 437px; top: 975px; width: 190px; height: 27px; border-radius: 14px;
    background: var(--pink); color: var(--white); font: 700 15px/27px "Montserrat", sans-serif; text-align: center;
    box-shadow: 0 2px 3px rgba(0,0,0,.25);
  }
  .fine-print { position: absolute; left: 42px; top: 1007px; font: italic 400 14px/1.25 "Arimo", sans-serif; color: var(--white); }

  .feature-ring { position: absolute; left: 0; top: 0; width: 1026px; height: 1200px; }
  .feature-photo {
    position: absolute; left: 700px; top: 800px; width: 720px; height: 720px; border-radius: 50%;
    background: radial-gradient(circle at 30% 30%, #efe9e2, #8f6f57 40%, #2c2622 60%, #9aa0a8 85%);
  }

  .contacts { position: absolute; top: 1071px; font: 400 13px/1.3 "Arimo", sans-serif; color: #222; text-align: center; }
  .contacts .name { font-weight: 700; color: var(--pink); }
  .contact-left { left: 55px; width: 210px; }
  .contact-right { left: 385px; width: 200px; }
  .divider { position: absolute; left: 365px; top: 1071px; width: 1px; height: 106px; background: #bbbbbb; }
  .signature { width: 80px; height: 22px; margin: 8px auto 0; background: linear-gradient(90deg, #d7d0e6, #b9a8d6); border-radius: 3px; }
  .small-org { margin-top: 4px; font: 700 9px/1.2 "Arimo", sans-serif; color: #222; }
  .small-org.spaced { margin-top: 12px; }
</style>
</head>
<body>
<main class="flyer">
  <div class="hero-photo" role="img" aria-label="Volunteers outdoors washing a shaggy grey dog on a sudsy pavement"></div>

  <svg class="swoosh" viewBox="0 0 1026 1200" aria-hidden="true">
    <path fill="var(--purple)" d="M0,402 C300,318 650,330 1026,418 L1026,1200 L0,1200 Z"/>
    <path fill="var(--pink)" d="M0,418 C300,334 650,346 1026,434 L1026,1200 L0,1200 Z"/>
    <path fill="var(--white)" d="M0,434 C300,350 650,362 1026,450 L1026,1200 L0,1200 Z"/>
  </svg>

  <div class="spot-photo spot-dog" role="img" aria-label="German shepherd dog on grass"></div>
  <div class="spot-photo spot-music" role="img" aria-label="Musicians performing at the event"></div>
  <div class="spot-photo spot-mascot" role="img" aria-label="Children posing with a dog mascot"></div>

  <p class="kicker">THIRD ANNUAL</p>
  <h1 class="title">MAPLE &amp; CLOVER</h1>
  <p class="subtitle">DOGGIE WASH EXTRAVAGANZA</p>
  <p class="tagline-pill">A FAMILY FUN EVENT FOR ALL AGES</p>

  <aside class="support">
    <p class="support-label">IN SUPPORT OF</p>
    <p class="partner-name"><span class="mark"></span><span>Circle of Harlow Ridge Pet Center</span></p>
    <p class="partner-note">Adopt a forever friend…<br>You will be their hero</p>
  </aside>

  <div class="details when">
    <span class="label">Date:</span>
    <span>Saturday, April 25<sup>th</sup>, 2020<br>Rain Date May 2<sup>nd</sup></span>
  </div>
  <div class="details time">
    <span class="label">Time:</span>
    <span>10 am- 1pm</span>
  </div>
  <div class="details where">
    <span class="label">Location:</span><br>
    Linden Realty, 418 Harborline<br>Ave. Cedar Bay FL 32990<br>Wrenfield Town Center
  </div>

  <div class="perks-band"></div>
  <ul class="perks perks-left">
    <li><svg viewBox="0 0 26 26"><rect x="2" y="12" width="22" height="8" rx="3" fill="var(--pink)"/><rect x="4" y="4" width="4" height="9" fill="var(--pink)"/><rect x="5" y="20" width="3" height="4" fill="var(--pink)"/><rect x="18" y="20" width="3" height="4" fill="var(--pink)"/></svg>FREE Doggie Wash</li>
    <li><svg viewBox="0 0 26 26"><path d="M3,19 A10,10 0 0 1 23,19 Z" fill="var(--pink)"/><rect x="1" y="20" width="24" height="3" fill="var(--pink)"/><circle cx="13" cy="7" r="2" fill="var(--pink)"/></svg>Food &amp; Beverages</li>
    <li><svg viewBox="0 0 26 26"><rect x="3" y="4" width="20" height="6" fill="var(--pink)"/><rect x="4" y="11" width="18" height="12" fill="var(--pink)"/><rect x="10" y="15" width="6" height="8" fill="var(--green)"/></svg>Vendors (FREE give-a-ways)</li>
  </ul>
  <ul class="perks perks-right">
    <li><svg viewBox="0 0 26 26"><rect x="2" y="6" width="22" height="14" rx="3" fill="var(--pink)"/></svg>Raffle Drawings</li>
    <li><svg viewBox="0 0 26 26"><rect x="3" y="8" width="20" height="5" fill="var(--pink)"/><rect x="5" y="13" width="16" height="10" fill="var(--pink)"/><rect x="12" y="8" width="2" height="15" fill="var(--green)"/><circle cx="10" cy="5" r="3" fill="var(--pink)"/><circle cx="16" cy="5" r="3" fill="var(--pink)"/></svg>Grand Prize</li>
    <li><svg viewBox="0 0 26 26"><rect x="1" y="7" width="24" height="13" rx="1" fill="none" stroke="var(--pink)" stroke-width="2.5"/><circle cx="13" cy="13.5" r="3.5" fill="var(--pink)"/></svg>Donations Welcome</li>
  </ul>
  <p class="donate-line">To make a donation: www.socialpage.com/CHRPC</p>
  <p class="donate-button">CLICK: DONATE</p>
  <p class="fine-print">All domestic breeds from pupies to seniors invited.<br>Please be sure Furry Fido is tolerant of other dogs, crowds and bathing.</p>

  <svg class="feature-ring" viewBox="0 0 1026 1200" aria-hidden="true">
    <circle cx="1060" cy="1160" r="380" fill="var(--purple)"/>
    <circle cx="1060" cy="1160" r="367" fill="var(--white)"/>
    <circle cx="1060" cy="1160" r="366" fill="var(--pink)"/>
  </svg>
  <div class="feature-photo" role="img" aria-label="Young woman drying a small black and tan puppy in a white towel"></div>

  <section class="contacts contact-left">
    <p class="name">DANA WHITLOCK</p>
    <p>Linden Realty Corp.</p>
    <p>555.201.4417</p>
    <p>dana.whitlock@lindenrealty.com</p>
    <div class="signature" role="img" aria-label="Handwritten signature"></div>
    <p class="small-org">Linden Realty</p>
  </section>
  <div class="divider"></div>
  <section class="contacts contact-right">
    <p class="name">MARISA KELLEN</p>
    <p>CHRPC</p>
    <p>555.318.2260</p>
    <p>marisa.kellen@mailbay.net</p>
    <p class="small-org spaced">Circle of Harlow Ridge<br>Pet Center</p>
  </section>
</main>
</body>
</html>
```